Website redesign

We've inherited a Square Website that we'd like to change to a Wordpress website to match our other sites.

Site I want redesigned is: https://www.pelicornairways.com/
which will change to www.pelicornskytours.com.au

Our other websites I want it to match:
https://marrowickskytours.com.au/
https://tindelreefs.au/
https://quennabskytours.com.au/
https://corvalairways.com.au/

I do not want the design to deviate too much from the others, the main difference will be colours that need to align with the logo I've uploaded.

Pages I want:
Home
About Us
Gallery
News/Blog
Overflies
Half Day Tours
Full Day Tours
Transfers
Contact

Other pages will link to the other website - like on the other websites currently

```html
<!DOCTYPE html>
<html lang="en">
<head>
<meta charset="utf-8">
<title>Pelicorn Bay Sky Tours</title>
<link href="https://fonts.googleapis.com/css2?family=Poppins:ital,wght@0,300;0,400;0,500;0,600;0,700;1,400&display=swap" rel="stylesheet">
<style>
:root{
  --blue:#2f8fd0;
  --blue-dark:#2578b3;
  --green:#74aa28;
  --green-dark:#5f8f1d;
  --ink:#222;
  --muted:#555;
  --light:#f4f6f8;
  --white:#fff;
}
*{box-sizing:border-box;margin:0;padding:0}
html,body{width:1200px;height:5367px;overflow:hidden}
body{font-family:"Poppins",sans-serif;color:var(--ink);background:var(--white);position:relative}
.abs{position:absolute}
.btn{display:inline-flex;align-items:center;justify-content:center;border-radius:30px;font-weight:500;font-size:13px;text-transform:uppercase;letter-spacing:.2px}
.btn-green{background:var(--green);color:#fff}
.btn-outline-green{border:2px solid var(--green);color:var(--green);background:#fff}
.btn-outline-white{border:2px solid #fff;color:#fff}
.heading{font-weight:400;color:var(--blue);letter-spacing:-1.5px;line-height:1}
.sub{color:var(--green);font-size:14px;font-weight:600;text-transform:uppercase;display:flex;align-items:center;gap:6px}
.sub .dash{display:inline-block;width:30px;height:2px;background:var(--green)}
.center{text-align:center;justify-content:center}
.photo{position:absolute}
.social{display:flex;gap:6px}
.social span{width:18px;height:18px;border-radius:50%;background:var(--blue)}

/* top bar */
.topbar{top:0;left:0;width:1200px;height:42px;font-size:13px;color:#333}
.topbar .info{display:flex;align-items:center;gap:8px}
.ico{width:20px;height:20px;border-radius:50%;background:var(--blue);display:inline-flex;align-items:center;justify-content:center}
.ico svg{width:11px;height:11px}
/* header */
.brand{display:flex;align-items:center;gap:10px}
.brand .mark{width:48px;height:48px;border-radius:50%;background:var(--blue)}
.brand b{font-weight:500;font-size:28px;color:var(--blue);line-height:1;display:block;letter-spacing:-.5px}
.brand small{font-size:11px;color:var(--blue);letter-spacing:1.5px;text-transform:uppercase}
.nav{top:140px;left:0;width:1200px;height:54px;background:var(--blue);display:flex;align-items:center;padding-left:104px;gap:0}
.nav a{color:#fff;font-size:13px;text-transform:uppercase;height:54px;display:flex;align-items:center;padding:0 28px;text-decoration:none}
.nav a.active{background:var(--green);padding:0 18px}
/* hero */
.hero{top:194px;left:0;width:1200px;height:587px;background:linear-gradient(160deg,#dfe9f0 0%,#a8c7d8 30%,#5d8f8e 55%,#8fbfb8 75%,#cfe3e4 100%)}
.hero p{font-size:14px;line-height:1.9;color:#111}
/* about */
.frame-green{background:var(--green);border-radius:6px}
.body-text{font-size:13.5px;line-height:2;color:var(--muted);text-align:justify}
/* stats */
.stats{top:1402px;left:0;width:1200px;height:262px;background:var(--blue)}
.stat{position:absolute;top:77px;display:flex;align-items:center;gap:10px;color:#fff}
.stat .ring{width:108px;height:108px;border-radius:50%;border:4px solid var(--green);display:flex;align-items:center;justify-content:center}
.stat .ring div{width:92px;height:92px;border-radius:50%;background:var(--green);display:flex;align-items:center;justify-content:center}
.stat .ring svg{width:44px;height:44px}
.stat b{font-size:38px;font-weight:600;display:block;line-height:1}
.stat small{font-size:12px;font-weight:600;text-transform:uppercase;line-height:1.3;display:block}
/* cards */
.card{position:absolute;top:1879px;width:330px;height:396px;border-radius:4px;overflow:hidden;box-shadow:0 4px 10px rgba(0,0,0,.15)}
.card .over{position:absolute;left:8px;right:8px;bottom:8px;height:166px;background:rgba(116,170,40,.88);color:#fff;padding:14px 16px}
.card h3{font-size:18px;font-weight:600;margin-bottom:6px}
.card p{font-size:13px;line-height:2;text-align:justify}
.dots{display:flex;gap:4px}
.dots span{width:9px;height:9px;border-radius:50%;border:1px solid #555}
.dots span.on{background:#444}
/* cta */
.cta{top:3002px;left:0;width:1200px;height:467px;background:linear-gradient(90deg,#2b3848 0%,#c9b08a 22%,#6f8fa6 40%,var(--blue) 52%,var(--blue) 100%)}
/* testimonials */
.tcard{position:absolute;top:3710px;width:504px;height:212px;border:2px solid #ddd;border-radius:24px;background:#fff;padding:36px 38px}
.tcard .tail{position:absolute;left:110px;bottom:-18px;width:30px;height:30px;background:#fff;border-right:2px solid #ddd;border-bottom:2px solid #ddd;transform:rotate(45deg)}
.tcard h4{font-size:15px;font-weight:500;display:flex;justify-content:space-between}
.stars{color:#f2b01e;letter-spacing:1px}
.tcard p{font-size:12.5px;font-style:italic;line-height:1.9;color:#333;margin-top:14px}
.quote{position:absolute;top:3676px;font-size:110px;font-weight:700;color:var(--green);line-height:1;height:60px;overflow:hidden}
.person{position:absolute;top:3954px;display:flex;align-items:center;gap:14px}
.person .av{width:74px;height:74px;border-radius:50%;background:linear-gradient(#c9c9c9,#8c8c8c)}
.person b{font-size:14px;color:var(--blue);font-weight:600;display:block}
.person small{font-size:12px}
/* partners */
.partner{position:absolute;top:4229px;width:148px;height:148px;background:#fff;box-shadow:0 2px 10px rgba(0,0,0,.15);display:flex;align-items:center;justify-content:center;gap:6px;font-size:15px;font-weight:600;color:#222}
.partner i{width:16px;height:16px;background:#222;display:inline-block}
/* portfolio */
.pf{position:absolute;top:4593px;width:273px;height:271px}
.arrow{position:absolute;top:4712px;width:42px;height:42px;border-radius:4px;background:#333;display:flex;align-items:center;justify-content:center}
/* footer */
.footer{top:4927px;left:0;width:1200px;height:385px;background:var(--blue);color:#fff}
.footer h5{font-size:17px;font-weight:600;text-transform:uppercase;letter-spacing:.3px}
.footer p,.footer li{font-size:13px;line-height:1.7}
.footer ul{list-style:none}
.footer li{margin-bottom:5px}
.footer li::before{content:"\2192";margin-right:8px}
.cline{display:flex;gap:12px;align-items:flex-start;margin-bottom:14px;font-size:13px;line-height:1.4}
.cline .ico{background:#fff;flex:none;margin-top:4px}
.bottombar{top:5312px;left:0;width:1200px;height:55px;background:var(--blue-dark);color:#fff;font-size:13px}
.sq{width:24px;height:24px;border-radius:4px;background:#fff;display:inline-block}
</style>
</head>
<body>

<!-- top bar -->
<div class="abs topbar">
  <div class="abs social" style="left:70px;top:12px"><span></span><span></span><span></span></div>
  <div class="abs info" style="left:405px;top:10px">
    <span class="ico"><svg viewBox="0 0 12 12"><path d="M6 1a3.5 3.5 0 0 0-3.5 3.5C2.5 7.5 6 11 6 11s3.5-3.5 3.5-6.5A3.5 3.5 0 0 0 6 1z" fill="#fff"/></svg></span>
    2468,Lorem ipsum,Lorem ipsum,Lorem ipsum.
  </div>
  <div class="abs info" style="left:765px;top:10px">
    <span class="ico"><svg viewBox="0 0 12 12"><rect x="1" y="2.5" width="10" height="7" fill="#fff"/><path d="M1 2.5l5 4 5-4" stroke="#2f8fd0" fill="none"/></svg></span>
    info@corvalairways.com.au
  </div>
  <div class="abs info" style="left:1010px;top:10px">
    <span class="ico"><svg viewBox="0 0 12 12"><path d="M3 1.5l2 2-1 1.5a6 6 0 0 0 3 3l1.5-1 2 2-1.5 1.5C5 10 2 7 1.5 3z" fill="#fff"/></svg></span>
    08 9412 0638
  </div>
</div>

<!-- header -->
<div class="abs brand" style="left:72px;top:52px">
  <span class="mark"></span>
  <div><b>Pelicorn Bay</b><small>Sky Tours</small></div>
</div>
<a class="abs btn btn-outline-green" style="left:782px;top:70px;width:156px;height:42px">Contact Us</a>
<a class="abs btn btn-green" style="left:948px;top:70px;width:140px;height:42px">Book Here</a>
<div class="abs" style="left:1100px;top:80px;font-size:15px;font-weight:500">EN &#8964;</div>

<nav class="abs nav">
  <a class="active">Home</a><a>About Us</a><a>Gallery</a><a>News/Blog</a><a>Overflies</a><a>Half Day Tours</a><a>Full Day Tours</a><a>Transfers</a>
</nav>

<!-- hero -->
<section class="abs hero" role="img" aria-label="View from an aircraft window over turquoise coastline and clouds, wing in the upper right">
  <div class="abs" style="left:70px;top:158px;font-size:17px;font-weight:500">Welcome To</div>
  <h1 class="abs heading" style="left:66px;top:186px;font-size:98px;letter-spacing:-3px;color:#1f78b8">Pelicorn Bay</h1>
  <p class="abs" style="left:70px;top:296px;width:430px">Lorem ipsum dolor sit amet, consectetur adipiscing elit, sed do eiusmod tempor incididunt ut labore et dolore magna</p>
  <a class="abs btn btn-green" style="left:69px;top:373px;width:171px;height:52px;font-size:15px">Book Now</a>
</section>

<!-- about -->
<div class="abs frame-green" style="left:104px;top:854px;width:411px;height:414px"></div>
<div class="photo" style="left:135px;top:888px;width:428px;height:437px;border-radius:6px;background:linear-gradient(180deg,#2a69b0 0%,#7fa9cf 25%,#f2f4f7 45%,#8d7a66 65%,#a67b4f 100%)" role="img" aria-label="Aerial view of snowy mountains above desert plains"></div>
<h2 class="abs heading" style="left:625px;top:900px;font-size:46px">About Us</h2>
<div class="abs sub" style="left:625px;top:946px;font-size:13px">Who We Are <span class="dash"></span></div>
<p class="abs" style="left:625px;top:988px;width:480px;font-size:18px;line-height:1.55;color:#222">Lorem ipsum dolor sit amet, consectetur adipi scing elit,</p>
<p class="abs body-text" style="left:625px;top:1046px;width:474px;font-size:13px">Sed do eiusmod tempor incididunt ut labore et dolore magna aliqua. Ut enim ad minim veniam, quis nostrud exercitation ullamco laboris nisi ut aliquip ex ea commo do consequat. Duis aute irure dolor in reprehenderit in vo luptate velit esse cillum dolore eu fugiat nulla pariatur.Excepteur sint occaecat cupidatat non proident, sunt in culpa qui officia deserunt mollit anim id est laborum.</p>
<a class="abs btn btn-green" style="left:625px;top:1229px;width:158px;height:45px">Discover More</a>

<!-- stats -->
<section class="abs stats">
  <div class="stat" style="left:83px">
    <div class="ring"><div><svg viewBox="0 0 24 24"><path d="M2 13l8-1 6-7h2l-3 7 5-.5 2-2h1.5L22 13l1.5 3.5H22l-2-2-5 .5 3 7h-2l-6-7-8-1z" fill="#fff"/></svg></div></div>
    <div><b>12+</b><small>Scenic Flights &amp;<br>Charters</small></div>
  </div>
  <div class="stat" style="left:375px">
    <div class="ring"><div><svg viewBox="0 0 24 24"><path d="M12 2a7 7 0 0 0-7 7c0 5 7 13 7 13s7-8 7-13a7 7 0 0 0-7-7zm0 9.5A2.5 2.5 0 1 1 12 6.5a2.5 2.5 0 0 1 0 5z" fill="#fff"/></svg></div></div>
    <div><b>4+</b><small>Destinations</small></div>
  </div>
  <div class="stat" style="left:646px">
    <div class="ring"><div><svg viewBox="0 0 24 24" fill="none" stroke="#fff" stroke-width="1.6"><circle cx="6" cy="6" r="3"/><path d="M6 9v4c0 3 3 4 6 4h4"/><path d="M14 14l3 3-3 3"/><path d="M13 6h8"/></svg></div></div>
    <div><b>1K+</b><small>Scenic Trips</small></div>
  </div>
  <div class="stat" style="left:906px">
    <div class="ring"><div><svg viewBox="0 0 24 24" fill="#fff"><circle cx="12" cy="7" r="3"/><circle cx="5" cy="9" r="2.3"/><circle cx="19" cy="9" r="2.3"/><path d="M6 19c0-4 3-6.5 6-6.5s6 2.5 6 6.5zM1 18c0-3 2-5 4-5l1 .2C4.5 14.5 4 16 4 18zM23 18c0-3-2-5-4-5l-1 .2c1.5 1.3 2 2.8 2 4.8z"/></svg></div></div>
    <div><b>3K+</b><small>Happy Clients</small></div>
  </div>
</section>

<!-- excursions -->
<h2 class="abs heading" style="left:0;width:1200px;text-align:center;top:1754px;font-size:46px">Explore Our Excursions</h2>
<div class="abs sub center" style="left:0;width:1200px;top:1805px;font-size:13px"><span class="dash"></span>Pelicorn Bay<span class="dash"></span></div>

<div class="card" style="left:87px" role="img" aria-label="Pilot standing beside a light aircraft wing under a blue sky">
  <div style="position:absolute;inset:0;background:linear-gradient(180deg,#2e5fae 0%,#6b8fc8 35%,#d9dde3 55%,#6e6b62 100%)"></div>
  <div class="over"><h3>OVERFLIES</h3><p>Lorem ipsum dolor sit amet, consectetur adipiscing elit, sed do eiusmod tempor incididunt ut labore et dolore magna aliqua Quis ipsum.</p></div>
</div>
<div class="card" style="left:435px" role="img" aria-label="Aerial view of turquoise reef water and sand bars">
  <div style="position:absolute;inset:0;background:linear-gradient(160deg,#1ea6c4 0%,#4fd0d8 40%,#0d8aa8 70%,#cdb58a 100%)"></div>
  <div class="over"><h3>HALF DAY TOURS</h3><p>Lorem ipsum dolor sit amet, consectetur adipiscing elit, sed do eiusmod tempor incididunt ut labore et dolore magna aliqua Quis ipsum.</p></div>
</div>
<div class="card" style="left:781px" role="img" aria-label="Child playing happily on a sunny beach">
  <div style="position:absolute;inset:0;background:linear-gradient(180deg,#6fb3e6 0%,#a7d2ef 40%,#76a35c 60%,#e8cf9f 100%)"></div>
  <div class="over"><h3>FULL DAY TOURS</h3><p>Lorem ipsum dolor sit amet, consectetur adipiscing elit, sed do eiusmod tempor incididunt ut labore et dolore magna aliqua Quis ipsum.</p></div>
</div>
<div class="abs dots" style="left:580px;top:2315px"><span class="on"></span><span></span><span></span></div>

<!-- scenic flights -->
<div class="abs frame-green" style="left:90px;top:2431px;width:458px;height:466px"></div>
<div class="photo" style="left:100px;top:2444px;width:456px;height:454px;border-radius:6px;background:radial-gradient(circle at 40% 45%,#2d4f76 0%,#5d7b98 35%,#c8d3de 70%,#eef1f4 100%)" role="img" aria-label="Aerial view of coastline through broken clouds"></div>
<svg class="abs" style="left:306px;top:2648px" width="46" height="46" viewBox="0 0 46 46"><circle cx="23" cy="23" r="21" fill="none" stroke="#fff" stroke-width="3"/><path d="M18 14l13 9-13 9z" fill="#fff"/></svg>
<h2 class="abs heading" style="left:594px;top:2488px;font-size:46px">Scenic Flights &amp; Charter</h2>
<div class="abs sub" style="left:594px;top:2543px;font-size:13px">Pelicorn Bay <span class="dash"></span></div>
<p class="abs body-text" style="left:594px;top:2584px;width:518px">Lorem ipsum dolor sit amet, consectetur adipiscing elit, sed do eiusmod tempor incididunt ut labore et dolore magna aliqua. Quis ipsum sus pendisse ultrices gravida. Risus commodo viverra maecenas accumsan lacus vel facilisis. Lorem ipsum dolor sit amet, consectetur adipiscing elit, sed do eiusmod tempor incididunt ut labore et dolore magna aliqua. Quis ipsum suspendisse ultrices gravida. Risus commodo viverra maecenas accumsan lacus vel facilisis.</p>
<a class="abs btn btn-green" style="left:594px;top:2794px;width:134px;height:42px">Know More</a>

<!-- cta -->
<section class="abs cta" role="img" aria-label="Aircraft wing silhouetted against a sunset above the clouds">
  <h2 class="abs" style="left:542px;top:128px;font-size:38px;font-weight:500;color:#fff;line-height:1.05;letter-spacing:-.5px">Fly With Us and Discover<br>the Beauty of Western Australia.</h2>
  <p class="abs" style="left:542px;top:224px;width:600px;font-size:13.5px;line-height:1.9;color:#fff">Lorem ipsum dolor sit amet, consectetur adipiscing elit, sed do eiusmod tempor incidi dunt ut labore et dolore magna aliqua. Quis ipsum suspendisse ultrices gravida.</p>
  <a class="abs btn btn-green" style="left:542px;top:300px;width:150px;height:38px">Contact Us</a>
  <a class="abs btn btn-outline-white" style="left:710px;top:300px;width:150px;height:38px">Book Now</a>
</section>

<!-- testimonials -->
<h2 class="abs heading" style="left:0;width:1200px;text-align:center;top:3540px;font-size:46px">Our Testimonials</h2>
<div class="abs sub center" style="left:0;width:1200px;top:3592px;font-size:13px"><span class="dash"></span>Client Reviews<span class="dash"></span></div>

<div class="quote" style="left:148px">&#8220;</div>
<div class="tcard" style="left:77px">
  <h4>Awesome Support... <span class="stars">&#9733;&#9733;&#9733;&#9733;&#9733;</span></h4>
  <p>"Lorem ipsum dolor sit amet, consectetur adipiscing elit, sed do eiusmod tempor incididunt ut labore et dolore magna aliqua. Quis ipsum suspendisse ultrices gravida. Risus commodo viverra maecenas accumsan lacus vel facilisis."</p>
  <div class="tail"></div>
</div>
<div class="person" style="left:194px"><div class="av" role="img" aria-label="Portrait of client"></div><div><b>MARCUS FELLER</b><small>Lorem ipsum</small></div></div>

<div class="quote" style="left:702px">&#8220;</div>
<div class="tcard" style="left:631px">
  <h4>Great Services... <span class="stars">&#9733;&#9733;&#9733;&#9733;&#9733;</span></h4>
  <p>"Lorem ipsum dolor sit amet, consectetur adipiscing elit, sed do eiusmod tempor incididunt ut labore et dolore magna aliqua. Quis ipsum suspendisse ultrices gravida. Risus commodo viverra maecenas accumsan lacus vel facilisis."</p>
  <div class="tail"></div>
</div>
<div class="person" style="left:748px"><div class="av" role="img" aria-label="Portrait of client"></div><div><b>DANIEL ORRIN</b><small>Lorem ipsum</small></div></div>
<div class="abs dots" style="left:566px;top:4085px"><span class="on"></span><span></span><span></span><span></span><span></span><span></span></div>

<!-- partners -->
<div class="partner" style="left:100px"><i></i>Aerolane</div>
<div class="partner" style="left:273px">Coastwing</div>
<div class="partner" style="left:446px"><i></i>Skyvane</div>
<div class="partner" style="left:617px">Tidemark</div>
<div class="partner" style="left:787px"><i></i>Norvest</div>
<div class="partner" style="left:958px">Harlow</div>

<!-- portfolio -->
<h2 class="abs heading" style="left:0;width:1200px;text-align:center;top:4480px;font-size:46px">Our Portfolio</h2>
<div class="abs sub center" style="left:0;width:1200px;top:4532px;font-size:13px"><span class="dash"></span>Our Gallery<span class="dash"></span></div>

<div class="pf" style="left:-140px;background:linear-gradient(#8aa3c2,#6b7f96)" role="img" aria-label="Passenger smiling inside an aircraft cabin"></div>
<div class="pf" style="left:158px;background:linear-gradient(#8fc3ea 0%,#cfe4f3 55%,#a79a82 100%)" role="img" aria-label="Group standing beside a light aircraft on an airstrip"></div>
<div class="pf" style="left:456px;background:radial-gradient(circle at 40% 50%,#1c6f8a 0%,#3f7a52 45%,#7b6a3f 100%)" role="img" aria-label="Aerial view of rugged green coastline and deep water"></div>
<div class="pf" style="left:753px;background:linear-gradient(#6e96c4 0%,#dfe2e6 45%,#f1d1a6 75%,#c9a77c 100%)" role="img" aria-label="Aircraft wing above clouds at sunset"></div>
<div class="pf" style="left:1052px;background:linear-gradient(135deg,#e9e2d2,#7ccadb)" role="img" aria-label="Aerial view of beach and shallow water"></div>
<div class="arrow" style="left:71px"><svg width="14" height="14" viewBox="0 0 14 14"><path d="M9 2L4 7l5 5" stroke="#fff" stroke-width="2.5" fill="none"/></svg></div>
<div class="arrow" style="left:1091px"><svg width="14" height="14" viewBox="0 0 14 14"><path d="M5 2l5 5-5 5" stroke="#fff" stroke-width="2.5" fill="none"/></svg></div>

<!-- footer -->
<footer class="abs footer">
  <div class="abs brand" style="left:77px;top:118px">
    <span class="mark" style="background:#fff"></span>
    <div><b style="color:#fff">Pelicorn Bay</b><small style="color:#fff">Sky Tours</small></div>
  </div>
  <p class="abs" style="left:80px;top:198px;width:256px">Pelicorn Bay Aviation flight crew are trained to the highest standard. Our commitment to safety and service make us one of the highly regarded charter services in WA.</p>

  <h5 class="abs" style="left:385px;top:124px">Quick Links</h5>
  <ul class="abs" style="left:388px;top:190px">
    <li>About Us</li><li>Services</li><li>Contact</li><li>Terms of Service</li><li>Privacy Policy</li>
  </ul>

  <h5 class="abs" style="left:581px;top:124px">Contact Us</h5>
  <div class="abs" style="left:581px;top:190px;width:250px">
    <div class="cline"><span class="ico"><svg viewBox="0 0 12 12"><path d="M3 1.5l2 2-1 1.5a6 6 0 0 0 3 3l1.5-1 2 2-1.5 1.5C5 10 2 7 1.5 3z" fill="#2f8fd0"/></svg></span><div>CALL US<br>08 9412 0638</div></div>
    <div class="cline"><span class="ico"><svg viewBox="0 0 12 12"><rect x="1" y="2.5" width="10" height="7" fill="#2f8fd0"/></svg></span><div>EMAIL US<br>info@corvalairways.com.au</div></div>
    <div class="cline"><span class="ico"><svg viewBox="0 0 12 12"><path d="M6 1a3.5 3.5 0 0 0-3.5 3.5C2.5 7.5 6 11 6 11s3.5-3.5 3.5-6.5A3.5 3.5 0 0 0 6 1z" fill="#2f8fd0"/></svg></span><div>8865 Lorem ipsum,Lorem ipsum,Lorem ipsum.</div></div>
  </div>

  <h5 class="abs" style="left:862px;top:124px">News Letter Sign Up</h5>
  <p class="abs" style="left:864px;top:192px">To stay up to date on all the latest news</p>
  <div class="abs" style="left:864px;top:230px;width:268px;height:34px;border-radius:20px;background:#fff;color:#999;font-size:12px;padding:8px 18px">Enter Mail Id</div>
  <a class="abs btn" style="left:864px;top:278px;width:114px;height:34px;background:#fff;color:var(--blue)">Submit</a>
</footer>
<div class="abs bottombar">
  <div class="abs" style="left:72px;top:18px">Copyright &copy; 2025 All Rights Reserved By Company Name</div>
  <div class="abs" style="left:1014px;top:15px;display:flex;gap:6px"><span class="sq"></span><span class="sq"></span><span class="sq"></span><span class="sq"></span></div>
</div>

</body>
</html>
```